Designs for a Barrister's chambers

Design stationery (including business card and letterhead) for a barrister's chambers -- similar to a law firm, using the enclosed logo. The current designs are not fit for purpose.

```html
<!DOCTYPE html>
<html lang="en">
<head>
<meta charset="utf-8">
<title>Ledgerwick Chambers – Business Card</title>
<link rel="stylesheet" href="https://fonts.googleapis.com/css2?family=Poppins:wght@400;500;600&display=swap">
<style>
  :root {
    --stage: #b9b9b9;
    --paper: #ffffff;
    --navy: #0e1828;
    --navy-soft: #16233a;
    --ink: #1a2436;
    --teal: #1693b2;
    --rule: #2a3447;
    --faint: #eef2f5;
  }
  * { box-sizing: border-box; margin: 0; padding: 0; }
  html, body { width: 1200px; height: 801px; overflow: hidden; }
  body {
    background: var(--stage);
    font-family: "Poppins", sans-serif;
    color: var(--ink);
    position: relative;
  }
  .card {
    position: absolute;
    top: 252px;
    width: 520px;
    height: 297px;
    border-radius: 3px;
    overflow: hidden;
    box-shadow: 0 10px 24px rgba(0,0,0,.22);
  }
  .card--front { left: 50px; background: var(--paper); }
  .card--back { left: 630px; background: var(--navy); }

  .front__decoration {
    position: absolute;
    top: 0; right: 0;
    width: 230px; height: 170px;
    background: radial-gradient(ellipse at 70% 30%, var(--faint) 0%, rgba(238,242,245,0) 70%);
  }

  .brand {
    position: absolute;
    display: flex;
    align-items: center;
    gap: 12px;
  }
  .brand__square { width: 38px; height: 38px; background: var(--teal); flex: none; }
  .brand__name {
    font-weight: 600;
    font-size: 22px;
    line-height: 1.05;
    letter-spacing: -.2px;
  }
  .card--front .brand { left: 34px; bottom: 56px; }
  .card--front .brand__name { color: var(--navy); }
  .card--back .brand { right: 34px; bottom: 48px; }
  .card--back .brand__name { color: #ffffff; font-size: 24px; }

  .person { position: absolute; left: 238px; top: 54px; width: 250px; }
  .person__name { font-weight: 600; font-size: 21px; color: var(--navy); line-height: 1.15; }
  .person__role { font-weight: 500; font-size: 15px; color: var(--teal); line-height: 1.3; }
  .person__rule { height: 1px; background: var(--rule); margin: 12px 0 13px; width: 226px; }

  .contacts { list-style: none; }
  .contacts li {
    display: flex;
    align-items: center;
    gap: 8px;
    font-size: 9.5px;
    font-weight: 500;
    color: var(--ink);
    line-height: 1.25;
    margin-bottom: 6px;
    white-space: nowrap;
  }
  .contacts .icon {
    width: 15px; height: 15px;
    border-radius: 3px;
    background: var(--teal);
    flex: none;
    display: flex; align-items: center; justify-content: center;
  }
  .contacts .icon svg { width: 9px; height: 9px; }

  .back__texture {
    position: absolute; inset: 0;
    background: radial-gradient(ellipse at 25% 70%, var(--navy-soft) 0%, var(--navy) 65%);
  }
</style>
</head>
<body>

  <section class="card card--front" aria-label="Business card front">
    <div class="front__decoration" role="img" aria-label="Faint large brand watermark"></div>

    <div class="brand">
      <span class="brand__square"></span>
      <span class="brand__name">Ledgerwick<br>Chambers</span>
    </div>

    <div class="person">
      <h1 class="person__name">Marcus Hollowell</h1>
      <p class="person__role">Barrister</p>
      <div class="person__rule"></div>
      <ul class="contacts">
        <li>
          <span class="icon"><svg viewBox="0 0 10 10"><path d="M2.2 1 3.8 2.8 3 4a5 5 0 0 0 3 3l1.2-.8L9 7.8 8 9C4.5 9 1 5.5 1 2Z" fill="#fff"/></svg></span>
          <span>0203 555 0142<br>07700 900 318</span>
        </li>
        <li>
          <span class="icon"><svg viewBox="0 0 10 10"><rect x="1" y="2.2" width="8" height="5.6" fill="none" stroke="#fff" stroke-width="1"/><path d="M1 2.4 5 5.6 9 2.4" fill="none" stroke="#fff" stroke-width="1"/></svg></span>
          <span>marcus.hollowell@ledgerwickchambers.com</span>
        </li>
        <li>
          <span class="icon"><svg viewBox="0 0 10 10"><circle cx="5" cy="5" r="3.8" fill="none" stroke="#fff" stroke-width="1"/><ellipse cx="5" cy="5" rx="1.6" ry="3.8" fill="none" stroke="#fff" stroke-width=".9"/><path d="M1.2 5h7.6" stroke="#fff" stroke-width=".9"/></svg></span>
          <span>www.ledgerwickchambers.com</span>
        </li>
        <li>
          <span class="icon"><svg viewBox="0 0 10 10"><path d="M5 9.4C3 7 2 5.5 2 4a3 3 0 0 1 6 0c0 1.5-1 3-3 5.4Z" fill="#fff"/><circle cx="5" cy="4" r="1.1" fill="#1693b2"/></svg></span>
          <span>48 Tallow Lane, London EC4Y 7BN</span>
        </li>
      </ul>
    </div>
  </section>

  <section class="card card--back" aria-label="Business card back">
    <div class="back__texture" role="img" aria-label="Embossed repeating brand pattern on dark navy"></div>
    <div class="brand">
      <span class="brand__square"></span>
      <span class="brand__name">Ledgerwick<br>Chambers</span>
    </div>
  </section>

</body>
</html>
```